Design some Business Cards for Corvane Tech Group

I would like a nicely designed business card template for my re-branded business, 'Corvane Tech Group'.

I would like it to be a standard landscape design to fit on 88.5*50mm PVC plastic cards:

I've attached our business logo files, if the design could match their style and color scheme while making good aesthetic use of the transparent plastic medium they will be printed on that would be fantastic.

```html
<!DOCTYPE html>
<html lang="en">
<head>
<meta charset="utf-8">
<title>Corvane Tech Group – Business Card</title>
<link href="https://fonts.googleapis.com/css2?family=Open+Sans:wght@400;600&display=swap" rel="stylesheet">
<style>
  :root {
    --backdrop: #232426;
    --panel-blue: #2c3f97;
    --panel-blue-deep: #26378a;
    --frost: #c9ccd0;
    --frost-edge: #e3e5e8;
    --accent-green: #2f9a48;
    --rule-green: #3fae57;
    --brand-blue: #2379c2;
    --text-light: #eef1fb;
  }
  * { box-sizing: border-box; margin: 0; padding: 0; }
  html, body {
    width: 1200px; height: 800px; overflow: hidden;
    background: var(--backdrop);
    font-family: "Open Sans", sans-serif;
  }
  .card {
    position: absolute; left: 157px; top: 150px;
    width: 885px; height: 500px;
    border-radius: 26px;
    background: linear-gradient(135deg, var(--frost-edge), var(--frost));
    overflow: hidden;
  }
  .card__panel {
    position: absolute; left: 0; top: 0;
    width: 400px; height: 100%;
    background: linear-gradient(160deg, var(--panel-blue), var(--panel-blue-deep));
  }
  .holder {
    position: absolute; left: 150px; top: 46px;
    color: var(--text-light);
  }
  .holder__name { font-size: 27px; font-weight: 400; line-height: 1.1; }
  .holder__company { font-size: 16px; font-weight: 400; margin-left: 22px; margin-top: 2px; }
  .contact {
    position: absolute; right: 0; width: 400px; height: 70px;
  }
  .contact__text {
    position: absolute; right: 92px; bottom: 12px;
    color: var(--text-light); font-size: 17px; white-space: nowrap;
  }
  .contact__rule {
    position: absolute; right: 70px; bottom: 0; width: 260px; height: 1px;
    background: var(--rule-green);
  }
  .contact__icon {
    position: absolute; right: 0; top: 0;
    width: 70px; height: 70px;
    background: var(--accent-green);
    display: flex; align-items: center; justify-content: center;
  }
  .contact--home { top: 210px; }
  .contact--phone { top: 284px; }
  .contact--web { top: 358px; }
  .brand {
    position: absolute; left: 470px; top: 180px; width: 380px;
    display: flex; align-items: center; gap: 20px;
  }
  .brand__dot {
    flex: none; width: 64px; height: 64px; border-radius: 50%;
    background: var(--accent-green);
  }
  .brand__name {
    color: var(--brand-blue); font-size: 44px; font-weight: 600; line-height: 1.05;
  }
</style>
</head>
<body>
  <div class="card">
    <div class="card__panel">
      <div class="holder">
        <div class="holder__name">Marek Oduya</div>
        <div class="holder__company">Larkfield Consulting</div>
      </div>

      <div class="contact contact--home">
        <span class="contact__text">Flag of UEA and Flag of UK</span>
        <span class="contact__rule"></span>
        <span class="contact__icon">
          <svg width="34" height="30" viewBox="0 0 34 30"><path d="M17 2 L32 15 H27 V28 H20 V20 H14 V28 H7 V15 H2 Z" fill="#fff"/></svg>
        </span>
      </div>

      <div class="contact contact--phone">
        <span class="contact__text">00971 555 010274</span>
        <span class="contact__rule"></span>
        <span class="contact__icon">
          <svg width="30" height="30" viewBox="0 0 30 30"><path d="M8 3 L12 10 L9 13 C11 18 13 20 17 22 L20 19 L27 23 L24 28 C14 27 4 17 3 7 Z" fill="#fff"/></svg>
        </span>
      </div>

      <div class="contact contact--web">
        <span class="contact__text">Marek.Oduya@larkfield.com</span>
        <span class="contact__rule"></span>
        <span class="contact__icon">
          <svg width="36" height="28" viewBox="0 0 36 28"><rect x="6" y="3" width="24" height="16" fill="none" stroke="#fff" stroke-width="2.5"/><path d="M2 22 H34 L31 26 H5 Z" fill="#fff"/></svg>
        </span>
      </div>

      <div class="contact" style="top:432px;height:50px;">
        <span class="contact__text" style="bottom:14px;">www.larkfield.com</span>
      </div>
    </div>

    <div class="brand">
      <span class="brand__dot"></span>
      <span class="brand__name">Corvane Tech Group</span>
    </div>
  </div>
</body>
</html>
```